Geschäftspapiere für Vermittlung von Kindern und Jugendlichen für Werbung und TV
Zielgruppe
Vermittlung von Kindern und Jugendlichen für Werbung und TV
Aufgabenstellung
bestehendes Logo beibehalten

```html
<!DOCTYPE html>
<html lang="de">
<head>
<meta charset="utf-8">
<title>Kunterbunt Kids – Briefbogen</title>
<link rel="stylesheet" href="https://fonts.googleapis.com/css2?family=Open+Sans:wght@400;600;700&family=Roboto:wght@300;400&display=swap">
<style>
  :root {
    --backdrop: #d9dadb;
    --paper: #f3f3f3;
    --green: #86bc5a;
    --purple: #8e4a9a;
    --grey: #9a9a9a;
    --ink: #2e2e2e;
    --footer-ink: #3a3a3a;
    --rule: #c9a98a;
    --fold: #b9b9b9;
  }
  * { margin: 0; padding: 0; box-sizing: border-box; }
  html, body {
    width: 1024px; height: 1200px; overflow: hidden;
    background: var(--backdrop);
    font-family: "Open Sans", sans-serif;
  }
  .letterhead {
    position: absolute; left: 109px; top: 30px;
    width: 806px; height: 1140px;
    background: var(--paper);
    box-shadow: 0 6px 18px rgba(0,0,0,0.12);
    overflow: hidden;
  }
  .top-band {
    position: absolute; left: 0; top: 0; width: 100%; height: 28px;
    background: var(--green);
    color: #fff; font-size: 11.5px; line-height: 28px;
    padding-left: 67px;
  }
  .brand {
    position: absolute; right: 40px; top: 46px; text-align: right;
  }
  .brand-name {
    display: flex; align-items: center; justify-content: flex-end; gap: 10px;
    font-size: 30px; font-weight: 400; color: var(--purple); line-height: 1.1;
  }
  .brand-dot { width: 14px; height: 14px; border-radius: 50%; background: var(--green); }
  .brand-tagline {
    font-size: 14px; color: var(--grey); letter-spacing: 0.4px; margin-top: 4px;
  }
  .sender-line {
    position: absolute; left: 81px; top: 181px;
    font-size: 8.5px; font-weight: 600; color: var(--ink);
  }
  .fold-mark {
    position: absolute; left: 0; width: 12px; height: 1px; background: var(--fold);
  }
  .fold-mark.upper { top: 409px; }
  .fold-mark.middle { top: 578px; }
  .fold-mark.lower { top: 814px; }
  .letter-body {
    position: absolute; left: 75px; top: 446px; width: 640px;
    font-family: "Roboto", sans-serif; font-weight: 300;
    font-size: 16px; line-height: 21px; color: var(--ink);
  }
  .letter-body p { margin-bottom: 21px; }
  .signature {
    position: absolute; left: 70px; top: 808px; width: 154px; height: 60px;
    background: #e3e3e3; border-radius: 4px;
  }
  .footer {
    position: absolute; left: 0; top: 1056px; width: 100%; height: 64px;
    font-size: 8.6px; line-height: 12.4px; color: var(--footer-ink);
  }
  .footer-col { position: absolute; top: 0; }
  .footer-col.company { left: 65px; }
  .footer-col.contact { left: 241px; }
  .footer-col.register { left: 436px; top: 6px; }
  .footer-col.bank { left: 600px; }
  .footer-col strong { font-weight: 700; }
  .footer-divider {
    position: absolute; top: 0; width: 1px; height: 60px; background: var(--rule);
  }
  .contact-row { display: flex; align-items: center; gap: 6px; }
  .contact-row svg { width: 8px; height: 8px; flex: none; }
  .contact.footer-col { top: 6px; }
  .bottom-band {
    position: absolute; left: 0; bottom: 0; width: 100%; height: 6px;
    background: var(--purple);
  }
</style>
</head>
<body>
<main class="letterhead">
  <div class="top-band">Kunterbunt Kids Kindermodelagentur ein Unternehmen der Morgenstern Medien</div>

  <div class="brand">
    <div class="brand-name"><span class="brand-dot"></span>Kunterbunt Kids</div>
    <div class="brand-tagline">KINDERMODELAGENTUR</div>
  </div>

  <div class="sender-line">Kunterbunt Kids • Lindenweg 12 • 47230 Auenstadt</div>

  <span class="fold-mark upper"></span>
  <span class="fold-mark middle"></span>
  <span class="fold-mark lower"></span>

  <section class="letter-body">
    <p>Dear Valued Customer:</p>
    <p>Our records show that you have been a customer of Bright Harbor Group. since our grand opening last year. We would like to thank you for your business by inviting you to our preferred customer Spring Extravaganza next Saturday.</p>
    <p>Saturday's sales event is by invitation only. All of our stock, ...............................and bedding will be marked down from 50-80% off.* Doors open at 9:00 AM sharp. Complimentary coffee and donuts will be served. Public admission will commence at noon.</p>
    <p>We look forward to seeing you on Saturday. Please bring this invitation with you and present it at the door.</p>
    <p>Sincerely,</p>
  </section>

  <div class="signature" role="img" aria-label="Handwritten signature of the managing director"></div>

  <footer class="footer">
    <div class="footer-col company">
      <strong>Talentvermittlung Auen GmbH</strong><br>
      Lindenweg 12<br>
      47230 Auenstadt<br>
      Geschäftsführung:<br>
      Marlene Hofbauer-Kranz
    </div>
    <span class="footer-divider" style="left:212px"></span>
    <div class="footer-col contact">
      <div class="contact-row">
        <svg viewBox="0 0 10 10"><path d="M2 1 L4 1 L4.6 3.2 L3.4 4 Q4.3 5.8 6 6.6 L6.8 5.4 L9 6 L9 8 Q9 9 8 9 Q1 8.5 1 2 Q1 1 2 1Z" fill="var(--footer-ink)"/></svg>
        0203 555 180 24
      </div>
      <div class="contact-row">
        <svg viewBox="0 0 10 10"><rect x="2.5" y="1" width="5" height="3" fill="none" stroke="var(--footer-ink)"/><rect x="1" y="4" width="8" height="4" fill="var(--footer-ink)"/><rect x="2.5" y="6.5" width="5" height="3" fill="#fff" stroke="var(--footer-ink)"/></svg>
        0203 555 180 25
      </div>
      <div class="contact-row">
        <svg viewBox="0 0 10 10"><rect x="1" y="2" width="8" height="6" fill="none" stroke="var(--footer-ink)"/><path d="M1 2 L5 5.5 L9 2" fill="none" stroke="var(--footer-ink)"/></svg>
        buchhaltung@kunterbunt-kids.de
      </div>
      <div class="contact-row">
        <svg viewBox="0 0 10 10"><circle cx="5" cy="5" r="4" fill="none" stroke="var(--footer-ink)"/><ellipse cx="5" cy="5" rx="1.8" ry="4" fill="none" stroke="var(--footer-ink)"/><path d="M1 5 H9" stroke="var(--footer-ink)"/></svg>
        www.kunterbunt-kids.de
      </div>
    </div>
    <span class="footer-divider" style="left:412px"></span>
    <div class="footer-col register">
      AG Auenstadt<br>
      HR-Nr.: HRB 58120<br>
      Ust.-ID: DE918273645<br>
      steuer-Nr.: 456/7781/2090
    </div>
    <span class="footer-divider" style="left:571px"></span>
    <div class="footer-col bank">
      Sparkasse Auenstadt<br>
      Konto: 1 00 4417 09<br>
      BLZ: 35520000<br>
      IBAN: DE44 3552 0000 0100 4417 09<br>
      BIC: SPAUDED1XXX
    </div>
  </footer>

  <div class="bottom-band"></div>
</main>
</body>
</html>
```